Savor Fair of dallas event poster for ticket sales

poster to highlight overview of event to post for advanced ticket sales. should incorporate our featured areas, food areas, music, kids and family stuff, logo files and past year examples, website for more details is http://savorfairexpo.org ... we dont have a theme look yet for this year but open to all ideas. past examples attached
Updates

A combination of still gathering feedback, low number of entries and many of the designs look the same and multiple entries of the same design but in different displayed scenarios.

Target Market(s)

pre ticket advanced sales demographic 18-60 foodie, family, music etc

Industry/Entity Type

Event

Font styles to use
Serif
Sans Serif
Decorative
Script

Colors

Designer to choose colors to be used in the design.

Requirements
Must have
• event date/times, tickets on sale now, featured areas, fun fun fun something for everyne

```html
<!DOCTYPE html>
<html lang="en">
<head>
<meta charset="utf-8">
<title>Savor Fair of Dallas – Event Poster</title>
<link rel="stylesheet" href="https://fonts.googleapis.com/css2?family=Alfa+Slab+One&family=Antonio:wght@300;400;700&family=Oswald:wght@300;400;500;600&family=Montserrat:wght@600&family=Roboto+Condensed:wght@700&display=swap">
<style>
  :root {
    --stage: #000000;
    --wood-light: #5e3a22;
    --wood-dark: #32200f;
    --navy: #1f2c6e;
    --navy-deep: #131a4a;
    --red: #d32027;
    --gold: #d4922c;
    --tan: #dcc08a;
    --bronze: #a88440;
    --yellow: #f5e11a;
    --white: #ffffff;
  }
  * { margin: 0; padding: 0; box-sizing: border-box; }
  html, body { width: 1200px; height: 1200px; overflow: hidden; background: var(--stage); }
  .poster {
    position: absolute; left: 295px; top: 64px; width: 631px; height: 1038px;
    background: linear-gradient(160deg, var(--wood-light) 0%, #4a2c18 45%, var(--wood-dark) 100%);
    overflow: hidden; font-family: 'Oswald', sans-serif; color: var(--white);
  }
  .poster-shapes { position: absolute; inset: 0; width: 631px; height: 1038px; }
  .side-rule { position: absolute; left: 0; top: 12px; width: 20px; height: 876px; background: var(--gold); border-radius: 0 6px 6px 0; }
  .edition, .slogan {
    position: absolute; left: 0; width: 631px; text-align: center;
    font-family: 'Alfa Slab One', serif; color: var(--white);
  }
  .edition { top: 48px; font-size: 25px; padding-left: 30px; }
  .slogan { top: 155px; font-size: 25px; padding-left: 30px; }
  .event-name {
    position: absolute; top: 86px; left: 0; width: 631px; padding-left: 30px; text-align: center;
    font-family: 'Alfa Slab One', serif; font-size: 40px; font-weight: 400; color: var(--navy); letter-spacing: 1px; white-space: nowrap;
  }
  .headline-rule { position: absolute; left: 37px; top: 237px; width: 278px; height: 5px; background: var(--red); }
  .tagline {
    position: absolute; left: 37px; top: 250px; font-family: 'Antonio', sans-serif; font-weight: 400;
    font-size: 37px; line-height: 38px; color: var(--white); letter-spacing: -0.5px; white-space: nowrap;
    transform: scaleX(.76); transform-origin: left top;
  }
  .dates {
    position: absolute; left: 34px; top: 338px; font-family: 'Oswald', sans-serif; font-weight: 300;
    font-size: 126px; line-height: 126px; color: transparent; -webkit-text-stroke: 3px var(--red); letter-spacing: 2px;
  }
  .month-band { position: absolute; left: 21px; top: 468px; width: 330px; height: 100px; background: var(--tan); opacity: .9; }
  .month {
    position: absolute; left: 37px; top: 468px; font-family: 'Antonio', sans-serif; font-weight: 700;
    font-size: 84px; line-height: 100px; color: var(--gold); white-space: nowrap;
    transform: scaleX(.74); transform-origin: left top;
  }
  .venue {
    position: absolute; left: 37px; top: 574px; font-family: 'Antonio', sans-serif; font-weight: 300;
    font-size: 22px; line-height: 25px; color: var(--white); white-space: nowrap;
    transform: scaleX(.84); transform-origin: left top;
  }
  .venue .name { display: block; margin-bottom: 10px; }
  .highlights {
    position: absolute; right: 8px; top: 232px; text-align: right; font-family: 'Alfa Slab One', serif;
    font-size: 19px; line-height: 25px; color: var(--white); list-style: none;
  }
  .featured { position: absolute; left: 437px; top: 738px; width: 190px; }
  .featured h2 { font-family: 'Oswald', sans-serif; font-weight: 500; font-size: 22px; color: var(--yellow); transform: scaleX(.82); transform-origin: left; white-space: nowrap; }
  .featured ul { display: grid; grid-template-columns: 102px 88px; margin-top: 6px; list-style: none; }
  .featured li { font-family: 'Oswald', sans-serif; font-size: 8.5px; line-height: 14.5px; color: var(--yellow); white-space: nowrap; }
  .tickets {
    position: absolute; left: 75px; top: 864px; width: 480px; height: 39px; background: var(--bronze);
    clip-path: polygon(0 0, 100% 0, 93% 100%, 0 100%);
    font-family: 'Montserrat', sans-serif; font-weight: 600; font-size: 22px; line-height: 39px;
    text-align: center; padding-right: 40px; color: var(--white); letter-spacing: .5px;
  }
  .web-band { position: absolute; left: 0; top: 904px; width: 631px; height: 50px; background: var(--navy-deep); text-align: center; }
  .web-band a { font-family: 'Roboto Condensed', sans-serif; font-weight: 700; font-size: 32px; line-height: 50px; color: var(--white); text-decoration: none; }
  .sponsors { position: absolute; left: 0; top: 954px; width: 631px; height: 84px; background: var(--red); display: flex; align-items: center; justify-content: space-around; padding: 0 10px; }
  .sponsor { font-family: 'Oswald', sans-serif; font-weight: 500; font-size: 15px; line-height: 17px; text-align: center; }
  .sponsor.hotel { color: #f2e6e6; font-weight: 400; }
  .sponsor.cooks { color: var(--navy); }
  .sponsor.play { color: var(--yellow); font-size: 17px; }
  .sponsor.grill { color: #f7c65a; }
  .sponsor.live { color: #111111; font-size: 22px; font-weight: 600; }
</style>
</head>
<body>
  <main class="poster">
    <svg class="poster-shapes" viewBox="0 0 631 1038">
      <polygon points="0,760 420,440 460,440 0,820" fill="#d4922c" opacity=".22"/>
      <polygon points="0,900 560,470 600,470 0,960" fill="#d4922c" opacity=".18"/>
      <polygon role="img" aria-label="Photo of festival crowd outdoors" points="0,904 0,860 230,690 631,690 631,904" fill="#3b4a78"/>
      <polygon points="505,280 631,156 631,400" fill="#d32027"/>
      <polygon points="560,325 631,255 631,275 572,334" fill="#d4922c" opacity=".7"/>
      <polygon points="465,504 581,384 631,432 631,528 541,604" fill="#dcc08a"/>
      <polygon role="img" aria-label="Photo of a guest enjoying festival food" points="429,244 560,352 449,488 313,368" fill="#2f5aa0"/>
      <polygon role="img" aria-label="Photo of a vendor serving at a food stall" points="401,460 557,592 429,716 293,568" fill="#5b6b4a"/>
      <polygon role="img" aria-label="Photo of a father and child at the festival" points="297,588 425,716 313,864 145,716" fill="#8a8a86"/>
    </svg>

    <div class="side-rule"></div>
    <p class="edition">THE 32nd ANNUAL</p>
    <h1 class="event-name">SAVOR FAIR OF DALLAS</h1>
    <p class="slogan">EXPERIENCE IT ALL!</p>

    <div class="headline-rule"></div>
    <p class="tagline">Dallas’ largest summertime<br>food festival</p>
    <p class="dates">22-24</p>
    <div class="month-band"></div>
    <p class="month">June 2018</p>
    <p class="venue"><span class="name">@ Gearhouse Live</span>2840 Meridian Park Blvd E, Dallas,<br>TX 75220</p>

    <ul class="highlights">
      <li>~ FOOD</li>
      <li>~ FAMILY</li>
      <li>~ MUSIC</li>
      <li>~ ART</li>
    </ul>

    <section class="featured">
      <h2>Featured areas include</h2>
      <ul>
        <li>- THE FOODIE EXPERIENCE</li><li>- SAVOR CURBSIDE</li>
        <li>- AROUND THE TOWN</li><li>- ARTISAN MARKET</li>
        <li>- GRILL YARD</li><li>- SAVOR MARKETPLACE</li>
        <li>- LATIN FLAVORS</li><li>- THE KIDS PLAY ZONE</li>
        <li>- FUEL</li>
      </ul>
    </section>

    <div class="tickets">TICKETS ON SALE NOW</div>
    <div class="web-band"><a href="http://savorfairexpo.org">www.savorfairexpo.org</a></div>

    <footer class="sponsors">
      <span class="sponsor hotel">Harbor Crest<br>Hotels</span>
      <span class="sponsor cooks">Young Cooks<br>Fund</span>
      <span class="sponsor play">Kids<br>Play Zone</span>
      <span class="sponsor grill">Grill<br>Yard</span>
      <span class="sponsor live">Gearhouse Live</span>
    </footer>
  </main>
</body>
</html>
```